Business card design and logo needed - Photographer

I take photos of weddings, rodeos, snowmobiling.
Need a card to hand out to prospective clients.
Industry/Entity Type
Business
Contact Information for Business Card
Marlon Pettibrook Photography
Requirements
Must have
- Bold
Black or white base.
My website. www.MarlonPettibrook.com
Should not have
- camera/ lens/ aperture blades

```html
<!DOCTYPE html>
<html lang="en">
<head>
<meta charset="utf-8">
<title>Marlon Pettibrook Photography – Business Card Options</title>
<link rel="stylesheet" href="https://fonts.googleapis.com/css2?family=Montserrat:wght@400;500;700;800&display=swap">
<style>
  :root {
    --ink: #0d0d0d;
    --paper: #ffffff;
    --mist: #d8dcde;
    --slate: #a9b1b4;
    --logo-grey: #bfc6c8;
    --stage-top: #b4bdc2;
    --stage-mid: #f1f3f4;
    --shadow: rgba(0, 0, 0, 0.45);
  }
  * { margin: 0; padding: 0; box-sizing: border-box; }
  html, body { width: 1200px; height: 900px; overflow: hidden; }
  body {
    position: relative;
    font-family: "Montserrat", Arial, sans-serif;
    background: linear-gradient(180deg, var(--stage-top) 0%, var(--stage-mid) 45%, var(--stage-mid) 55%, var(--stage-top) 100%);
  }
  .card {
    position: absolute;
    overflow: hidden;
    box-shadow: 6px 6px 8px var(--shadow);
  }
  .card--left { left: 123px; width: 376px; height: 217px; }
  .card--right { left: 708px; width: 371px; height: 214px; }
  .row-1 { top: 50px; }
  .row-2 { top: 331px; }
  .row-3 { top: 612px; }

  .card__top, .card__band { position: absolute; left: 0; width: 100%; }
  .card__top { top: 0; }
  .card__band { bottom: 0; }

  .brand {
    position: absolute;
    left: 0; width: 100%;
    text-align: center;
    font-weight: 800;
    font-size: 17px;
    letter-spacing: 0.5px;
    line-height: 1;
  }
  .contact {
    position: absolute;
    left: 0; width: 100%;
    text-align: center;
    line-height: 1;
  }
  .contact__name { font-weight: 700; font-size: 12.5px; letter-spacing: 0.2px; }
  .contact__details { font-weight: 500; font-size: 10px; margin-top: 4px; letter-spacing: 0.3px; }
  .contact__details span + span { margin-left: 10px; }

  /* card 1 – silver fade over black */
  .v-fade-silver .card__top { height: 132px; background: linear-gradient(180deg, #9fa8ab 0%, #e4e7e8 45%, #ffffff 100%); }
  .v-fade-silver .card__band { height: 85px; background: var(--ink); color: var(--paper); }
  .v-fade-silver .brand { top: 70px; color: var(--logo-grey); }
  .v-fade-silver .contact { top: 162px; color: var(--paper); }

  /* card 2 – white over black, dark mark */
  .v-bold-black .card__top { height: 112px; background: var(--paper); }
  .v-bold-black .card__band { height: 102px; background: var(--ink); }
  .v-bold-black .brand { top: 50px; color: var(--ink); }
  .v-bold-black .contact { top: 147px; color: var(--paper); }

  /* card 3 – black over mist */
  .v-night .card__top { height: 128px; background: var(--ink); }
  .v-night .card__band { height: 89px; background: var(--mist); }
  .v-night .brand { top: 60px; color: var(--logo-grey); }
  .v-night .contact { top: 159px; color: var(--paper); }

  /* card 4 – white over slate */
  .v-slate .card__top { height: 124px; background: var(--paper); }
  .v-slate .card__band { height: 90px; background: var(--slate); }
  .v-slate .brand { top: 58px; color: var(--logo-grey); }
  .v-slate .contact { top: 155px; color: var(--paper); }

  /* card 5 – white to black fade */
  .v-fade-dark .card__top { height: 140px; background: linear-gradient(180deg, #ffffff 0%, #e2e4e5 30%, #8a8f91 70%, var(--ink) 100%); }
  .v-fade-dark .card__band { height: 77px; background: var(--ink); }
  .v-fade-dark .brand { top: 62px; color: var(--logo-grey); }
  .v-fade-dark .contact { top: 161px; color: var(--paper); }

  /* card 6 – white over black, light mark */
  .v-classic .card__top { height: 112px; background: var(--paper); }
  .v-classic .card__band { height: 102px; background: var(--ink); }
  .v-classic .brand { top: 50px; color: var(--logo-grey); }
  .v-classic .contact { top: 147px; color: var(--paper); }
</style>
</head>
<body>

  <section class="card card--left row-1 v-fade-silver">
    <div class="card__top"></div>
    <div class="card__band"></div>
    <div class="brand">MARLON PETTIBROOK</div>
    <div class="contact">
      <p class="contact__name">MARLON PETTIBROOK PHOTOGRAPHY</p>
      <p class="contact__details"><span>306.555.0142</span><span>WWW.MARLONPETTIBROOK.COM</span></p>
    </div>
  </section>

  <section class="card card--right row-1 v-bold-black">
    <div class="card__top"></div>
    <div class="card__band"></div>
    <div class="brand">MARLON PETTIBROOK</div>
    <div class="contact">
      <p class="contact__name">MARLON PETTIBROOK PHOTOGRAPHY</p>
      <p class="contact__details"><span>306.555.0142</span><span>WWW.MARLONPETTIBROOK.COM</span></p>
    </div>
  </section>

  <section class="card card--left row-2 v-night">
    <div class="card__top"></div>
    <div class="card__band"></div>
    <div class="brand">MARLON PETTIBROOK</div>
    <div class="contact">
      <p class="contact__name">MARLON PETTIBROOK PHOTOGRAPHY</p>
      <p class="contact__details"><span>306.555.0142</span><span>WWW.MARLONPETTIBROOK.COM</span></p>
    </div>
  </section>

  <section class="card card--right row-2 v-slate">
    <div class="card__top"></div>
    <div class="card__band"></div>
    <div class="brand">MARLON PETTIBROOK</div>
    <div class="contact">
      <p class="contact__name">MARLON PETTIBROOK PHOTOGRAPHY</p>
      <p class="contact__details"><span>306.555.0142</span><span>WWW.MARLONPETTIBROOK.COM</span></p>
    </div>
  </section>

  <section class="card card--left row-3 v-fade-dark">
    <div class="card__top"></div>
    <div class="card__band"></div>
    <div class="brand">MARLON PETTIBROOK</div>
    <div class="contact">
      <p class="contact__name">MARLON PETTIBROOK PHOTOGRAPHY</p>
      <p class="contact__details"><span>306.555.0142</span><span>WWW.MARLONPETTIBROOK.COM</span></p>
    </div>
  </section>

  <section class="card card--right row-3 v-classic">
    <div class="card__top"></div>
    <div class="card__band"></div>
    <div class="brand">MARLON PETTIBROOK</div>
    <div class="contact">
      <p class="contact__name">MARLON PETTIBROOK PHOTOGRAPHY</p>
      <p class="contact__details"><span>306.555.0142</span><span>WWW.MARLONPETTIBROOK.COM</span></p>
    </div>
  </section>

</body>
</html>
```